Letter Head for accounting firm

We need letter head designed using our attached logo.

We also need the following information on the letterhead:

482 E Mill Rd. Danvers, OH 43762

HarborLedgerLtd.com

1-855-613-2907

Contact Information for Business Card

Use logo

Colors

Designer to choose colors to be used in the design.

Requirements
Must have
• Business Card - Should also have name and title - email address

```html
<!DOCTYPE html>
<html lang="en">
<head>
<meta charset="utf-8">
<title>Harbor Ledger Group Ltd — Letterhead</title>
<link href="https://fonts.googleapis.com/css2?family=Open+Sans:wght@300;400;600&display=swap" rel="stylesheet">
<style>
  :root {
    --backdrop: #ecedf0;
    --paper: #fbfcfd;
    --brand-blue: #1d8fe0;
    --bright-cyan: #13aef0;
    --pale-cyan: #cfeaf8;
    --ink-soft: #9a9ea4;
    --ink-body: #a3a7ad;
  }
  * { margin: 0; padding: 0; box-sizing: border-box; }
  html, body {
    width: 1200px; height: 1200px; overflow: hidden;
    background: var(--backdrop);
    font-family: "Open Sans", Arial, sans-serif;
  }
  .letterhead {
    position: absolute; left: 270px; top: 136px;
    width: 660px; height: 928px;
    background: var(--paper);
    overflow: hidden;
  }
  .header-wash {
    position: absolute; left: 0; top: 0; width: 100%; height: 130px;
    background: linear-gradient(to bottom, rgba(19,174,240,0.55) 0%, rgba(191,228,246,0.45) 40%, rgba(251,252,253,0) 100%);
  }
  .footer-wash {
    position: absolute; left: 0; bottom: 0; width: 100%; height: 300px;
    background: linear-gradient(to bottom, rgba(251,252,253,0) 0%, rgba(207,234,248,0.7) 55%, rgba(19,174,240,0.75) 100%);
  }
  .brand {
    position: absolute; left: 80px; top: 112px; width: 190px;
    display: flex; flex-direction: column; align-items: center;
    color: var(--brand-blue); font-weight: 600;
  }
  .brand-mark { width: 40px; height: 40px; background: var(--brand-blue); margin-bottom: 12px; }
  .brand-name { font-size: 13.5px; letter-spacing: 0.2px; white-space: nowrap; }
  .brand-rule { width: 100%; border-top: 1px solid var(--brand-blue); margin-top: 3px; }
  .brand-suffix { font-size: 8px; letter-spacing: 1px; margin-top: 1px; }
  .contact { position: absolute; left: 420px; top: 134px; list-style: none; color: var(--brand-blue); }
  .contact li { display: flex; align-items: center; height: 28px; }
  .contact svg { width: 12px; height: 12px; margin-right: 16px; fill: var(--brand-blue); flex: none; }
  .contact .email { font-size: 13px; }
  .contact .small { font-size: 9.5px; line-height: 12px; }
  .salutation {
    position: absolute; left: 84px; top: 290px;
    font-size: 32px; font-weight: 300; color: var(--ink-soft);
  }
  .body-copy { position: absolute; left: 86px; top: 358px; width: 488px; }
  .body-copy p {
    font-size: 10.4px; line-height: 17px; color: var(--ink-body);
    margin-bottom: 16px; text-align: justify;
  }
  .signature { position: absolute; left: 452px; top: 700px; }
  .signer-name { font-size: 16px; font-weight: 600; color: var(--brand-blue); }
  .signer-title { font-size: 9.5px; color: var(--ink-soft); }
</style>
</head>
<body>
  <main class="letterhead">
    <div class="header-wash" role="img" aria-label="Flowing blue wave decoration along the top edge"></div>
    <div class="footer-wash" role="img" aria-label="Flowing blue wave decoration along the bottom edge"></div>

    <header class="brand">
      <div class="brand-mark"></div>
      <div class="brand-name">HARBOR LEDGER GROUP</div>
      <div class="brand-rule"></div>
      <div class="brand-suffix">LTD</div>
    </header>

    <ul class="contact">
      <li class="email">
        <svg viewBox="0 0 24 24"><path d="M12 2a7 7 0 0 0-7 7c0 5 7 13 7 13s7-8 7-13a7 7 0 0 0-7-7zm0 9.5A2.5 2.5 0 1 1 12 6.5a2.5 2.5 0 0 1 0 5z"/></svg>
        name@harborledgerltd.com
      </li>
      <li class="small">
        <svg viewBox="0 0 24 24"><path d="M6.6 10.8a15 15 0 0 0 6.6 6.6l2.2-2.2a1 1 0 0 1 1-.25 11.4 11.4 0 0 0 3.6.57 1 1 0 0 1 1 1V20a1 1 0 0 1-1 1A17 17 0 0 1 3 4a1 1 0 0 1 1-1h3.5a1 1 0 0 1 1 1c0 1.25.2 2.45.57 3.6a1 1 0 0 1-.25 1z"/></svg>
        <span>482 E Mill Rd. Danvers,<br>OH 43762</span>
      </li>
      <li class="small">
        <svg viewBox="0 0 24 24"><path d="M2 5h20v14H2z M2 5l10 7 10-7" fill="none" stroke="#1d8fe0" stroke-width="2.4"/></svg>
        1-855-613-2907
      </li>
    </ul>

    <h1 class="salutation">Dear John,</h1>

    <section class="body-copy">
      <p>Lorem ipsum dolor sit amet, consectetur adipiscing elit. Nullam vitae diam ac sapien porta semper sit amet nec ex. Nulla dignissim tortor tellus, ac vestibulum felis consectetur ac. Pellentesque ac congue augue. Praesent convallis magna at nibh luctus, egestas tincidunt tortor congue. Nullam dignissim ligula varius lectus convallis lacinia. Nunc ut tortor faucibus, tincidunt felis quis, viverra nulla. Maecenas sapien libero, fringilla quis venenatis id, varius dignissim sem.</p>
      <p>Cras tristique sapien eu ipsum consectetur porttitor. Praesent blandit rhoncus mi. Nunc maximus bibendum mi, sed dignissim neque consectetur quis. In tempor lacinia egestas. Nullam quis diam tristique nisl gravida porttitor. Aenean pellentesque sollicitudin magna nec ultricies. Curabitur eleifend nisl id turpis ornare, nec lacinia nisl suscipit.</p>
      <p>Curabitur blandit, erat efficitur aliquet ultrices, augue sapien vulputate dolor, eget maximus lectus magna eget lacus. Phasellus sollicitudin interdum eros ac porttitor.</p>
    </section>

    <footer class="signature">
      <div class="signer-name">Your Name Here</div>
      <div class="signer-title">Creative Director</div>
    </footer>
  </main>
</body>
</html>
```